依頼詳細
私達が大事にしているバリューが「楽しさ」なので、それが伝わるような画像を制作してほしいです。
メールの上部に載せる画像、下部に載せる画像をセットで作成いただきたいです。
※イメージ図を添付しますのでご参照ください
記載項目
・社名(英語)
・年賀状らしい文字
− 謹賀新年
− 2020
ページ数
片面
希望イメージ
シンプル 複雑
単色 カラフル
暗い 明るい
日常 高級
遊び心 厳粛
未来的 伝統的
女性的 男性的
希望する色
黄・オレンジ系、メインにブランドカラーは黄色・赤・青・緑を使用してほしいです
納品ファイル
• 高解像度JPG (.jpg)
補足説明
まだ提案を集めたいと思いますので、期限を数日延期いたします。
たくさんのご応募ありがとうございました!!!
■ 選んだ理由

シンプルで非常にいいなと思います。
引き続き宜しくお願いいたします。

■ 提案者全員のお礼・コメント

ご提案ありがとうございました。
今回短時間にも関わらず、色んな提案を見ることが出来て、大変助かりました。
また依頼を出すこともあると思いますので、引き続き宜しくお願いいたします。

```html
<!DOCTYPE html>
<html lang="ja">
<head>
<meta charset="utf-8">
<title>Happy New Year 2020 — Bright Playworks</title>
<link rel="stylesheet" href="https://fonts.googleapis.com/css2?family=Rubik:wght@900&family=Roboto:wght@500;700&family=Noto+Sans+JP:wght@700&display=swap">
<style>
  :root {
    --paper: #ffffff;
    --petal-deep: #f2b6d0;
    --petal-mid: #f7cfe1;
    --petal-light: #fbe6ef;
    --ink: #1a1a1a;
    --jp-red: #c8102e;
    --brand-red: #e8262c;
    --brand-blue: #1f6fd1;
    --brand-yellow: #f7c41a;
    --brand-green: #2fae4a;
  }
  * { margin: 0; padding: 0; box-sizing: border-box; }
  html, body { width: 813px; height: 1200px; overflow: hidden; background: var(--paper); }
  .card {
    position: relative;
    width: 813px;
    height: 1200px;
    background: var(--paper);
    overflow: hidden;
  }
  .petals-top {
    position: absolute;
    left: 0; top: 0;
    width: 813px; height: 600px;
    background:
      radial-gradient(ellipse 260px 200px at 120px 150px, var(--petal-deep), transparent 70%),
      radial-gradient(ellipse 280px 210px at 690px 160px, var(--petal-deep), transparent 70%),
      radial-gradient(ellipse 300px 180px at 420px 60px, var(--petal-mid), transparent 72%),
      radial-gradient(ellipse 240px 160px at 80px 430px, var(--petal-mid), transparent 70%),
      radial-gradient(ellipse 240px 160px at 740px 450px, var(--petal-mid), transparent 70%),
      linear-gradient(180deg, var(--petal-light) 0%, rgba(251,230,239,0.6) 55%, rgba(255,255,255,0) 100%);
  }
  .petals-bottom {
    position: absolute;
    left: 0; bottom: 0;
    width: 813px; height: 300px;
    background:
      radial-gradient(ellipse 260px 150px at 150px 240px, var(--petal-deep), transparent 70%),
      radial-gradient(ellipse 280px 160px at 600px 250px, var(--petal-deep), transparent 70%),
      radial-gradient(ellipse 220px 120px at 380px 180px, var(--petal-mid), transparent 70%),
      linear-gradient(0deg, var(--petal-light) 0%, rgba(251,230,239,0.5) 60%, rgba(255,255,255,0) 100%);
  }
  .greeting {
    position: absolute;
    left: 0; top: 195px;
    width: 813px;
    text-align: center;
    color: var(--ink);
  }
  .year {
    font-family: "Rubik", sans-serif;
    font-weight: 900;
    font-size: 150px;
    line-height: 130px;
    letter-spacing: -2px;
  }
  .year .d1 { color: var(--brand-red); }
  .year .d2 { color: var(--brand-blue); }
  .year .d3 { color: var(--brand-yellow); }
  .year .d4 { color: var(--brand-green); }
  .headline {
    margin-top: 12px;
    font-family: "Roboto", sans-serif;
    font-weight: 700;
    font-size: 36px;
    line-height: 40px;
  }
  .kinga {
    margin-top: 4px;
    font-family: "Noto Sans JP", sans-serif;
    font-weight: 700;
    font-size: 26px;
    line-height: 34px;
    letter-spacing: 26px;
    padding-left: 26px;
    color: var(--jp-red);
  }
  .from {
    margin-top: 12px;
    font-family: "Roboto", sans-serif;
    font-weight: 500;
    font-size: 22px;
    line-height: 26px;
  }
  .company {
    margin-top: 4px;
    font-family: "Roboto", sans-serif;
    font-weight: 500;
    font-size: 34px;
    line-height: 40px;
  }
</style>
</head>
<body>
  <main class="card">
    <div class="petals-top" role="img" aria-label="Soft pink flower petals with pink fireworks and colourful confetti bursting across the top"></div>
    <div class="petals-bottom" role="img" aria-label="Soft pink flower petals along the bottom edge"></div>
    <section class="greeting">
      <h1 class="year"><span class="d1">2</span><span class="d2">0</span><span class="d3">2</span><span class="d4">0</span></h1>
      <p class="headline">Happy New Year</p>
      <p class="kinga">謹賀新年</p>
      <p class="from">from</p>
      <p class="company">Bright Playworks</p>
    </section>
  </main>
</body>
</html>
```